Health care technology software systems

We have a solid logo. We have company colors that will need to be used as well. We just need a great business card design. We sell to health plans but want to be modern
Updates

Need extra days to review

Target Market(s)

Health technology sector selling into Health Plans

Industry/Entity Type

Health Care Technology

Contact Information for Business Card

Name, title, address, phone number, email

Requirements
Must have
• Use of Kembrata corporate colors - Uploaded w/ our logos

```html
<!DOCTYPE html>
<html lang="en">
<head>
<meta charset="utf-8">
<title>Kembrata Business Card</title>
<link href="https://fonts.googleapis.com/css2?family=Open+Sans:wght@300;400;600&display=swap" rel="stylesheet">
<style>
  :root {
    --stage: #8d9093;
    --stage-dark: #5e6164;
    --card-dark: #242424;
    --pattern-light: #6a6a6a;
    --card-light: #ffffff;
    --ink: #2b2b2b;
    --brand-green: #7dc142;
    --brand-blue: #1ea6e0;
    --brand-navy: #3b5fb0;
    --radius: 34px;
  }
  html, body {
    margin: 0;
    padding: 0;
    width: 1187px;
    height: 1200px;
    overflow: hidden;
  }
  body {
    background: radial-gradient(ellipse at 50% 40%, var(--stage) 0%, var(--stage-dark) 100%);
    font-family: "Open Sans", sans-serif;
    position: relative;
  }
  .card {
    position: absolute;
    left: 153px;
    width: 880px;
    height: 503px;
    border-radius: var(--radius);
    overflow: hidden;
    box-shadow: 0 14px 30px rgba(0,0,0,0.35);
  }
  .card-front { top: 60px; background: var(--card-dark); }
  .card-back  { top: 637px; background: var(--card-light); color: var(--ink); }

  .front-pattern {
    position: absolute;
    inset: 0;
    background: linear-gradient(110deg, #1c1c1c 0%, #2c2c2c 45%, var(--pattern-light) 100%);
  }
  .wordmark {
    display: flex;
    align-items: center;
    gap: 18px;
    font-weight: 300;
    letter-spacing: 1px;
  }
  .wordmark .mark-dot {
    border-radius: 50%;
    background: var(--brand-blue);
    flex: none;
  }
  .front-logo {
    position: absolute;
    left: 50%;
    top: 50%;
    transform: translate(-50%, -50%);
    font-size: 92px;
    color: #ffffff;
  }
  .front-logo .mark-dot { width: 86px; height: 86px; }

  .back-logo {
    position: absolute;
    right: 60px;
    top: 46px;
    font-size: 64px;
    color: var(--ink);
  }
  .back-logo .mark-dot { width: 58px; height: 58px; }

  .holder {
    position: absolute;
    left: 80px;
    top: 300px;
  }
  .holder-name {
    margin: 0;
    font-size: 34px;
    font-weight: 600;
    color: var(--brand-navy);
  }
  .holder-name .surname { color: var(--brand-blue); }
  .holder-title {
    margin: 4px 0 0 26px;
    font-size: 19px;
    color: var(--ink);
  }

  .contact {
    position: absolute;
    left: 560px;
    top: 200px;
    font-size: 19px;
    line-height: 1.35;
  }
  .contact-address { margin: 0 0 18px; }
  .contact-list { list-style: none; margin: 0; padding: 0; }
  .contact-list li { display: flex; align-items: center; gap: 8px; }
  .contact-list svg { width: 18px; height: 18px; flex: none; }
</style>
</head>
<body>
  <section class="card card-front">
    <div class="front-pattern" role="img" aria-label="Repeating pattern of tonal ring shapes fading from black to grey"></div>
    <div class="wordmark front-logo"><span class="mark-dot"></span><span>kembrata</span></div>
  </section>

  <section class="card card-back">
    <div class="wordmark back-logo"><span class="mark-dot"></span><span>kembrata</span></div>

    <div class="holder">
      <h1 class="holder-name">Dana <span class="surname">Whitcombe</span></h1>
      <p class="holder-title">Founders</p>
    </div>

    <div class="contact">
      <p class="contact-address">Maple Falls, Oregon,<br>&nbsp;&nbsp;United States</p>
      <ul class="contact-list">
        <li>
          <svg viewBox="0 0 20 20"><path d="M4 2 l4 0 l1 4 l-2 2 q2 4 5 5 l2-2 l4 1 l0 4 q-10 1-14-14z" fill="var(--brand-green)"/></svg>
          +1-800-555-0142
        </li>
        <li>
          <svg viewBox="0 0 20 20"><rect x="1" y="4" width="18" height="12" fill="var(--brand-navy)"/><path d="M1 4 l9 7 l9-7" fill="none" stroke="#fff" stroke-width="1.5"/></svg>
          info@kembrata.com
        </li>
        <li>
          <svg viewBox="0 0 20 20"><circle cx="10" cy="10" r="8.5" fill="var(--brand-blue)"/><path d="M1.5 10h17M10 1.5q-5 8.5 0 17M10 1.5q5 8.5 0 17" fill="none" stroke="#fff" stroke-width="1"/></svg>
          www.kembrata.com
        </li>
      </ul>
    </div>
  </section>
</body>
</html>
```